Consulting Website

We are looking at renewing out company's website. we are an organizational development consulting firm that works within the Middle East and Africa. Our focus on on organizations within the Gulf area.

We are looking to having a simple, clean and attractive website. pictures should be relevant to our location.

We are also looking for a creative design, something that isn't just "another consulting website"
Updates

Thank you all for submitting your designs, following are some general comments;

- Having a veiled women on the intro is NOT a must
- have a picture with people is NOT a must too, we can use nature, symbols, places..anything really!
- Here are some sites i like;
brightwaveteams.example
http://www.harborlanehomes.example/
http://www.quillterrace.example/
http://www.verdano.example/

I hope these could give you some idea :)

thanks again.

Industry/Entity Type

It Company

Requirements
Must have
• Tabs for press, testimonials, products, resources and services.
pictures also should be relevant to the geographical location. i.e. veiled women, men in traditional costumes and so on.

It's very important that we MAINTAIN the corporate colors of the logo.
Should not have
• Clean and neat design!
i REALLY dont like crowded designs.

```html
<!DOCTYPE html>
<html lang="en">
<head>
<meta charset="utf-8">
<title>Orivanta Consulting</title>
<link href="https://fonts.googleapis.com/css2?family=Ubuntu:wght@400;500&display=swap" rel="stylesheet">
<style>
:root{
  --slate-dark:#4f6878;
  --slate:#6d8798;
  --slate-light:#94aab8;
  --nav-top:#6a8496;
  --nav-bottom:#3e5666;
  --page:#e9e9e9;
  --footer:#eeeeee;
  --text:#3a3a3a;
  --muted:#6b6b6b;
  --heading:#c2ad8b;
  --rule:#bdbdbd;
  --button:#c99685;
  --button-dark:#b07c6b;
  --field:#bcbcbc;
}
*{margin:0;padding:0;box-sizing:border-box}
html,body{width:960px;height:1200px;overflow:hidden}
body{position:relative;background:var(--page);font-family:"Ubuntu",sans-serif;color:var(--text)}
.abs{position:absolute}

.top-strip{left:0;top:0;width:960px;height:6px;background:var(--slate)}
.header{left:0;top:6px;width:960px;height:124px;background:linear-gradient(#f1f1f1,#e2e2e2)}
.brand{left:96px;top:24px;display:flex;align-items:center;gap:10px}
.brand-mark{width:46px;height:46px;background:var(--slate-light)}
.brand-name{font-size:30px;font-weight:400;color:var(--slate);letter-spacing:2px}

.search-panel{left:579px;top:6px;width:244px;height:40px;background:linear-gradient(#e6e9eb,#c9d3d9);border:2px solid var(--slate-light);border-top:none;border-radius:0 0 4px 4px;z-index:3}
.search-field{left:17px;top:6px;width:212px;height:24px;border-radius:12px;background:linear-gradient(var(--nav-bottom),var(--slate));display:flex;align-items:center;padding-left:13px;font-size:8px;color:#e8eef2}
.search-button{right:0;top:0;width:38px;height:24px;border-radius:0 12px 12px 0;background:linear-gradient(#a3b3bd,#7c8f9b)}

.nav-band{left:0;top:104px;width:960px;height:26px;background:var(--slate-light)}
.hero{left:0;top:130px;width:960px;height:404px;background:radial-gradient(ellipse at 50% 45%,#5c4f2e 0%,#2a2440 35%,#14101e 65%,#050408 100%);z-index:1}
.nav{left:93px;top:94px;width:768px;height:52px;border-radius:4px;border:1px solid #a9bcc8;background:linear-gradient(var(--nav-top),var(--nav-bottom));z-index:3;box-shadow:0 1px 3px rgba(0,0,0,.35)}
.nav a{position:absolute;top:0;height:50px;line-height:50px;color:#fff;font-size:11.5px;text-decoration:none;transform:translateX(-50%);white-space:nowrap}
.nav .sep{position:absolute;top:15px;width:1px;height:20px;background:#c5b48f}

.section-title{left:0;width:960px;height:30px}
.section-title .rule{position:absolute;top:15px;height:1px;background:var(--rule)}
.section-title .dot{position:absolute;top:12px;width:6px;height:6px;border-radius:50%;background:#b5b5b5}
.section-title h2{position:absolute;left:417px;width:151px;text-align:center;font-size:26px;font-weight:400;color:var(--heading);text-shadow:0 1px 0 #fff,0 -1px 1px #9d8c70;line-height:30px;white-space:nowrap}

.copy{left:92px;width:762px;font-size:9.3px;line-height:11.6px;color:var(--text)}
.read-more{width:63px;height:23px;border:1px solid #fff;outline:1px solid #b98a7a;background:linear-gradient(var(--button),var(--button-dark));color:#fff;font-size:7.5px;text-align:center;line-height:21px}

.bullet{font-size:9.3px;color:var(--text);display:flex;align-items:center;gap:8px}
.bullet::before{content:"";width:8px;height:8px;background:#c8c8c8;border:1px solid #adadad}

.footer{left:0;top:960px;width:960px;height:240px;background:var(--footer);border-top:1px solid #fff}
.col-title{font-size:10px;font-weight:400;color:var(--slate-dark);letter-spacing:.8px}
.col-rule{height:1px;background:var(--slate)}
.site-links{left:96px;top:1022px;font-size:9.3px;line-height:14.4px;color:var(--muted);list-style:none}
.social{left:254px;list-style:none}
.social li{display:flex;align-items:center;gap:8px;height:25.6px;font-size:9.3px;color:var(--muted)}
.social .icon{width:20px;height:20px;border-radius:50%;background:var(--slate);border:2px solid #d0d7dc}
.social .icon.feed{background:#c98a55}
.contact-intro{left:415px;top:1020px;width:166px;font-size:8.5px;line-height:11px;color:var(--muted)}
.field{left:415px;width:159px;height:25px;background:var(--field);border-radius:2px;font-size:7.5px;color:#444;padding-left:8px;line-height:25px}
.send{left:511px;top:1114px;width:63px;height:22px;border:1px solid #fff;outline:1px solid var(--nav-bottom);background:linear-gradient(var(--slate),var(--nav-bottom));color:#fff;font-size:7px;text-align:center;line-height:20px}
.divider{left:622px;top:986px;width:1px;height:186px;background:#c9c9c9}
.footer-brand{left:654px;top:994px;display:flex;align-items:center;gap:8px}
.footer-brand .mark{width:40px;height:40px;background:#b9b9b9}
.footer-brand .name{font-size:24px;color:#a9a9a9;letter-spacing:2px}
.info{left:600px;width:290px;text-align:center;font-size:8.8px;line-height:11px;color:var(--text)}
</style>
</head>
<body>

<div class="abs top-strip"></div>
<div class="abs header"></div>

<div class="abs brand">
  <div class="brand-mark"></div>
  <div class="brand-name">ORIVANTA</div>
</div>

<div class="abs search-panel">
  <div class="abs search-field">Search this site...
    <div class="abs search-button">
      <svg width="38" height="24" viewBox="0 0 38 24"><circle cx="17" cy="10" r="5" fill="none" stroke="#fff" stroke-width="2"/><line x1="21" y1="14" x2="26" y2="19" stroke="#fff" stroke-width="2.5" stroke-linecap="round"/></svg>
    </div>
  </div>
</div>

<div class="abs nav-band"></div>
<div class="abs hero" role="img" aria-label="Photograph of engraved brass vases and a decorative engraved plate in front of green draped fabric"></div>

<nav class="abs nav">
  <a style="left:102px">Home</a>
  <span class="sep" style="left:155px"></span>
  <a style="left:226px">About ORIVANTA</a>
  <span class="sep" style="left:301px"></span>
  <a style="left:358px">Offerings</a>
  <span class="sep" style="left:411px"></span>
  <a style="left:489px">Knowledge Base</a>
  <span class="sep" style="left:566px"></span>
  <a style="left:631px">Contact Us</a>
</nav>

<div class="abs section-title" style="top:577px">
  <span class="rule" style="left:0;width:400px"></span>
  <span class="dot" style="left:400px"></span>
  <h2>Who We Are</h2>
  <span class="dot" style="left:582px"></span>
  <span class="rule" style="left:588px;width:372px"></span>
</div>

<p class="abs copy" style="top:621px">Orivanta Consulting is a firm specialized in providing customized Organization Development solutions to companies in the Middle East and Africa. Recognizing the inability of imported models and solutions to solve problems that face companies in our region, Orivanta Consulting builds on international best practices and customizes them to create best-fit solutions that are capable of addressing challenges effectively.</p>
<p class="abs copy" style="top:668px">Orivanta Consulting provides Organization Development solutions addressing the "HOW - Soft Side" that is needed to achieve the "WHAT - Business Strategy" in a holistic manner. Orivanta Consulting work centers around building an organizational culture that is aligned with and supports the business strategy.</p>

<div class="abs read-more" style="left:781px;top:706px">Read More</div>

<div class="abs section-title" style="top:743px">
  <span class="rule" style="left:0;width:400px"></span>
  <span class="dot" style="left:400px"></span>
  <h2>What We Do</h2>
  <span class="dot" style="left:582px"></span>
  <span class="rule" style="left:588px;width:372px"></span>
</div>

<p class="abs copy" style="top:783px">Orivanta Consulting helps organization develop an aligned humanistic organization design that:</p>

<div class="abs bullet" style="left:92px;top:804px">Creates a culture of high performance</div>
<div class="abs bullet" style="left:92px;top:825px">Nurtures leaders &amp; builds human potential</div>
<div class="abs bullet" style="left:92px;top:846px">Induces innovation across all corporate practices</div>
<div class="abs bullet" style="left:494px;top:804px">Increases internal organization efficiencies</div>
<div class="abs bullet" style="left:494px;top:825px">Enhances organization agility</div>

<p class="abs copy" style="top:869px">Orivanta Consulting utilizes a collaborative consulting model in which consultants work hand in hand with our clients to help them build organizations that support achieving the business strategy.&nbsp; They support clients with the implementation of change initiatives and, most importantly, transfer knowledge and build internal client capability to lead future change programs.</p>

<div class="abs read-more" style="left:781px;top:904px">Read More</div>

<footer class="abs footer"></footer>

<h3 class="abs col-title" style="left:96px;top:989px">SITE LINKS</h3>
<div class="abs col-rule" style="left:96px;top:1008px;width:116px"></div>
<ul class="abs site-links">
  <li>Home</li><li>About ORIVANTA</li><li>Offerings</li><li>Knowledge Based</li><li>Contact Us</li><li>Privacy Policy</li><li>Disclaimer</li>
</ul>

<h3 class="abs col-title" style="left:254px;top:989px">CONNECT WITH US</h3>
<div class="abs col-rule" style="left:254px;top:1008px;width:116px"></div>
<ul class="abs social" style="top:1019px">
  <li><span class="icon"></span>Chatline</li>
  <li><span class="icon"></span>Friendwall</li>
  <li><span class="icon"></span>Worknet</li>
  <li><span class="icon feed"></span>Rss Feed</li>
</ul>

<h3 class="abs col-title" style="left:415px;top:989px">CONTACT US</h3>
<div class="abs col-rule" style="left:415px;top:1008px;width:162px"></div>
<p class="abs contact-intro">Have a question? Don't wait... contact us right away!</p>
<div class="abs field" style="top:1050px">Full Name</div>
<div class="abs field" style="top:1080px">Email Address</div>
<div class="abs send">SEND</div>

<div class="abs divider"></div>

<div class="abs footer-brand">
  <div class="mark"></div>
  <div class="name">ORIVANTA</div>
</div>
<p class="abs info" style="top:1049px;color:var(--muted)">Copyright &copy; 2012. All rights reserved.</p>
<p class="abs info" style="top:1071px">Coral Bay Road, Palm Court Tower,<br>3rd Floor, Office # 304<br>P.O. Box 40210, Harbor City</p>
<p class="abs info" style="top:1113px;color:var(--muted)">Phone: <b style="font-weight:500">+000 5550 1234</b></p>

</body>
</html>
```